Business Cards for cafe providing speciality coffee and food

I need a business card design for my husband’s businesses. He has two cafes in Brisbane. The business name is Copperleaf Roasting House. They sell high end specialty coffee as well as breakfast and lunch. All the food is cooked fresh, in house and they have strict quality controls for their coffee. I would like the business card to feature the address for both cafes, my husband’s phone number and the business’s instagram. The address for the first is 61 Wexley Crescent, Pine Hollow and the second is 23 Dorrit Avenue, Sallowmere. The Instagram handle is @copperleafroastinghouse and phone number is 0491326085. We already have a business logo that is attached.

Target Market(s)

All ages, higher disposable income and more likely to eat out regularly

Industry/Entity Type

Hospitality

Contact Information for Business Card

Must be suitable for both customers and suppliers

Font styles to use
Sans Serif

Colors

Designer to choose colors to be used in the design.

Requirements
Must have
• Owner’s name: Griff Tallant
• Addresses of both cafes: 61 Wexley Crescent, Pine Hollow and 23 Dorrit Avenue, Sallowmere
• Instagram handle: @copperleafroastinghouse
• Contact number: 0491326085
Nice to have
• Business logo

```html
<!DOCTYPE html>
<html lang="en">
<head>
<meta charset="utf-8">
<title>Copperleaf Roasting House — Business Card</title>
<link rel="stylesheet" href="https://fonts.googleapis.com/css2?family=Roboto:wght@300;400;700&display=swap">
<style>
  :root {
    --page: #ececec;
    --card-front: #e5dbcf;
    --card-back: #fbfbf9;
    --ink: #1d1d1d;
    --ink-soft: #4a4a4a;
    --rule: #c9c9c9;
  }
  * { box-sizing: border-box; margin: 0; padding: 0; }
  html, body {
    width: 1200px; height: 1069px; overflow: hidden;
    background: var(--page);
    font-family: "Roboto", sans-serif;
    color: var(--ink);
  }
  .stage {
    position: relative; width: 1200px; height: 1069px;
  }
  .card {
    position: absolute; left: 250px; width: 700px; height: 400px;
    box-shadow: 0 6px 18px rgba(0,0,0,0.12);
  }
  .card--front { top: 104px; background: var(--card-front); }
  .card--back { top: 564px; background: var(--card-back); }

  /* Front */
  .brand {
    position: absolute; left: 0; right: 0; top: 120px;
    display: flex; flex-direction: column; align-items: center; gap: 18px;
  }
  .brand__dot {
    width: 64px; height: 64px; border-radius: 50%; background: var(--ink);
  }
  .brand__name {
    font-weight: 700; font-size: 28px; letter-spacing: 1px; color: var(--ink);
    text-transform: uppercase;
  }
  .website {
    position: absolute; left: 0; right: 0; bottom: 44px; text-align: center;
    font-weight: 400; font-size: 17px; letter-spacing: 3px; color: var(--ink-soft);
  }

  /* Back */
  .back__brand {
    position: absolute; left: 40px; top: 0; width: 260px; height: 400px;
    display: flex; flex-direction: column; align-items: center; justify-content: center; gap: 14px;
  }
  .back__brand .brand__dot { width: 48px; height: 48px; }
  .back__brand .brand__name {
    font-size: 20px; text-align: center; line-height: 1.3;
  }
  .divider {
    position: absolute; left: 330px; top: 70px; width: 1px; height: 260px;
    background: var(--rule);
  }
  .contact {
    position: absolute; left: 370px; top: 96px; width: 310px;
  }
  .contact__name {
    font-weight: 700; font-size: 27px; text-transform: uppercase; letter-spacing: 0.5px;
    margin-bottom: 14px;
  }
  .contact__address {
    font-weight: 400; font-size: 16px; line-height: 1.35; color: var(--ink-soft);
    padding-left: 18px; margin-bottom: 12px;
  }
  .contact__line {
    display: flex; align-items: center; gap: 10px;
    font-size: 16px; color: var(--ink-soft); padding-left: 18px; line-height: 1.6;
  }
  .contact__icon { width: 14px; height: 14px; flex: none; }
  .contact__square {
    width: 13px; height: 13px; border: 1.6px solid var(--ink); border-radius: 3px; flex: none;
  }
</style>
</head>
<body>
<main class="stage">
  <section class="card card--front">
    <div class="brand">
      <span class="brand__dot"></span>
      <span class="brand__name">Copperleaf Roasting House</span>
    </div>
    <p class="website">www.copperleafroastinghouse</p>
  </section>

  <section class="card card--back">
    <div class="back__brand">
      <span class="brand__dot"></span>
      <span class="brand__name">Copperleaf<br>Roasting House</span>
    </div>
    <div class="divider"></div>
    <div class="contact">
      <h1 class="contact__name">Griff Tallant</h1>
      <p class="contact__address">61 Wexley Crescent<br>Pine Hollow and 23 Dorrit Avenue<br>Sallowmere</p>
      <p class="contact__line">
        <svg class="contact__icon" viewBox="0 0 24 24" aria-hidden="true"><path fill="#1d1d1d" d="M6.6 10.8c1.4 2.8 3.8 5.1 6.6 6.6l2.2-2.2c.3-.3.7-.4 1-.2 1.1.4 2.3.6 3.6.6.6 0 1 .4 1 1V20c0 .6-.4 1-1 1C10.6 21 3 13.4 3 4c0-.6.4-1 1-1h3.5c.6 0 1 .4 1 1 0 1.3.2 2.5.6 3.6.1.3 0 .7-.2 1z"/></svg>
        0491326085
      </p>
      <p class="contact__line">
        <span class="contact__square"></span>
        @copperleafroastinghouse
      </p>
    </div>
  </section>
</main>
</body>
</html>
```